Cell phone repair

you can please design me business card

size 3.5" x 2"

colors blue and red

fixit dash logo (you get from my website fixitdashhq.com )

"We Come To You!

It is very simple! You tell us what phone you have, And we come to fix it."

phone number: 412.586.3094

website: www.fixitdashhq.com

email: info@fixitdashhq.com

```html
<!DOCTYPE html>
<html lang="en">
<head>
<meta charset="utf-8">
<title>Fixit Dash Business Card</title>
<link rel="stylesheet" href="https://fonts.googleapis.com/css2?family=Montserrat:wght@600;700;800&family=Lato:wght@400;700&display=swap">
<style>
  :root {
    --red: #e8202a;
    --red-deep: #d81820;
    --blue: #29a9e0;
    --blue-soft: #4fb8e6;
    --ink: #111111;
    --paper: #ffffff;
    --stage: #e9eaec;
  }
  * { margin: 0; padding: 0; box-sizing: border-box; }
  html, body { width: 1200px; height: 902px; overflow: hidden; background: var(--stage); }
  .canvas { position: relative; width: 1200px; height: 902px; }
  .card {
    position: absolute; left: 250px; width: 700px; height: 400px;
    border-radius: 28px; overflow: hidden;
    box-shadow: 0 6px 18px rgba(0,0,0,.18);
  }
  .card--front { top: 34px; background: linear-gradient(35deg, var(--blue) 0%, #9a6a78 38%, var(--red) 70%, var(--red-deep) 100%); }
  .card--back { top: 468px; background: var(--paper); }

  .circuit-area {
    position: absolute; left: 0; bottom: 0; width: 300px; height: 260px;
    background: radial-gradient(ellipse at 0% 100%, rgba(120,210,245,.55), rgba(120,210,245,0) 70%);
  }
  .front-brand {
    position: absolute; left: 0; right: 0; top: 150px;
    display: flex; justify-content: center; align-items: center; gap: 16px;
  }
  .brand-name {
    font-family: "Montserrat", sans-serif; font-weight: 700;
    font-size: 54px; letter-spacing: .5px;
  }
  .front-brand .brand-name { color: var(--paper); }
  .brand-dot { width: 34px; height: 34px; border-radius: 50%; }
  .front-brand .brand-dot { border: 5px solid var(--paper); }
  .front-url {
    position: absolute; left: 0; right: 0; top: 240px; text-align: center;
    font-family: "Lato", sans-serif; font-size: 15px; letter-spacing: 2px; color: var(--paper);
  }

  .back-brand {
    position: absolute; left: 120px; top: 34px;
    display: flex; align-items: center; gap: 16px;
  }
  .back-brand .brand-name { color: var(--blue); font-size: 50px; }
  .back-brand .brand-square { width: 46px; height: 46px; border-radius: 6px; background: var(--red); }
  .headline {
    position: absolute; left: 150px; top: 112px;
    font-family: "Montserrat", sans-serif; font-weight: 800; font-size: 36px; color: var(--ink);
  }
  .subhead {
    position: absolute; left: 232px; top: 160px;
    font-family: "Montserrat", sans-serif; font-weight: 700; font-size: 22px; color: var(--red);
  }
  .tagline {
    position: absolute; left: 70px; top: 196px;
    font-family: "Montserrat", sans-serif; font-weight: 600; font-size: 19px; color: var(--blue);
  }
  .rule {
    position: absolute; left: 70px; top: 228px; width: 600px; height: 3px;
    background: linear-gradient(90deg, var(--red) 0%, var(--red) 45%, var(--blue) 60%, var(--blue) 100%);
  }
  .email {
    position: absolute; right: 40px; top: 240px;
    font-family: "Lato", sans-serif; font-size: 15px; color: var(--ink);
  }
  .call {
    position: absolute; left: 34px; top: 300px; padding-top: 6px;
    border-top: 3px solid var(--red);
  }
  .call-label { font-family: "Montserrat", sans-serif; font-weight: 700; font-size: 20px; color: var(--red); }
  .call-number { font-family: "Montserrat", sans-serif; font-weight: 700; font-size: 34px; color: var(--ink); line-height: 1.1; }
  .corner-band { position: absolute; right: 0; bottom: 0; width: 380px; height: 110px; }
  .corner-url {
    position: absolute; right: 40px; bottom: 30px;
    font-family: "Lato", sans-serif; font-size: 19px; color: var(--paper); letter-spacing: .5px;
  }
</style>
</head>
<body>
<main class="canvas">
  <section class="card card--front">
    <div class="circuit-area" role="img" aria-label="Soft circuit board line pattern in light blue"></div>
    <div class="front-brand">
      <span class="brand-name">Fixit Dash</span>
      <span class="brand-dot"></span>
    </div>
    <p class="front-url">WWW.FIXITDASHHQ.COM</p>
  </section>

  <section class="card card--back">
    <div class="back-brand">
      <span class="brand-name">Fixit Dash</span>
      <span class="brand-square"></span>
    </div>
    <h1 class="headline">We Come To You!</h1>
    <p class="subhead">It is very simple!</p>
    <p class="tagline">You tell us what phone you have, And we come to fix it.</p>
    <div class="rule"></div>
    <p class="email">info@fixitdashhq.com</p>
    <div class="call">
      <p class="call-label">CALL US</p>
      <p class="call-number">412.586.3094</p>
    </div>
    <svg class="corner-band" viewBox="0 0 380 110" preserveAspectRatio="none" aria-hidden="true">
      <defs>
        <linearGradient id="bandFill" x1="0" y1="0" x2="1" y2="0">
          <stop offset="0" stop-color="#e8202a"/>
          <stop offset=".35" stop-color="#e8202a"/>
          <stop offset=".6" stop-color="#d9dfe4"/>
          <stop offset="1" stop-color="#29a9e0"/>
        </linearGradient>
      </defs>
      <path d="M60 0 H380 V110 H0 Q30 10 60 0 Z" fill="url(#bandFill)"/>
    </svg>
    <p class="corner-url">www.fixitdashhq.com</p>
  </section>
</main>
</body>
</html>
```